Product Factsheet for waste management / recycling company

We are a waste management company that specialises in recycling products to farm land as an alternative to checmical fertilisers. Having just launched a new brand, we are looking to update our product factsheets which are sent out or given to farmers. Using our products can help significantly reduce or eliminate farmers chemical fertiliser costs and our services also provide additional benefits (soil analysis every 4 years, consistent pricing, no spreading costs (to farmers))
We would like a flyer that highlights the benefits of our products and reflects the green credentials of using recycled materials rather than chemical fertiliser.
We'd like to see clean proffessional designs that use green/blues to match our branding and logo. Factsheets must be A4 in size
I've attached copies of some of our old factsheet to illustrate the information that is provided but general feedback is that they are a bit too wordy and don't have enough impact.
Feel free to contact me if you have any questions
Target Market(s)
Farmers, landowners and agribusiness
Industry/Entity Type
Agriculture
Requirements
Must have
- Logo and tagline - Fertiliser doesn't cost the earth

```html
<!DOCTYPE html>
<html lang="en">
<head>
<meta charset="utf-8">
<title>Biosolids+ Factsheet</title>
<link href="https://fonts.googleapis.com/css2?family=Oswald:wght@500;700&family=Lato:wght@400;700;900&display=swap" rel="stylesheet">
<style>
  :root {
    --lime: #8cc63f;
    --lime-light: #a6d45e;
    --olive: #4f6b1e;
    --blue: #1b63ad;
    --blue-dark: #164f8c;
    --ink: #333333;
    --white: #ffffff;
    --paper: #ffffff;
  }
  * { box-sizing: border-box; margin: 0; padding: 0; }
  html, body { width: 900px; height: 1200px; overflow: hidden; background: var(--paper); }
  body { font-family: 'Lato', sans-serif; color: var(--ink); }

  .factsheet { position: relative; width: 900px; height: 1200px; background: var(--white); overflow: hidden; }

  .side-band { position: absolute; left: 0; top: 0; width: 194px; height: 1141px; background: var(--lime); }
  .side-band__title {
    position: absolute; left: 97px; top: 570px;
    transform: translate(-50%, -50%) rotate(-90deg);
    font-family: 'Oswald', sans-serif; font-weight: 700; font-size: 150px;
    letter-spacing: 22px; color: var(--olive); white-space: nowrap; line-height: 1;
  }
  .side-rule { position: absolute; left: 207px; top: 0; width: 4px; height: 1141px; background: var(--blue); }

  .content { position: absolute; left: 214px; top: 0; right: 0; }

  .hero { position: relative; height: 341px; }
  .hero__photo {
    position: absolute; inset: 0;
    background: linear-gradient(180deg, #7ea6cf 0%, #c9d7e3 22%, #9aa99a 38%, #5f7d3c 52%, #7fb43a 70%, #6b8a3a 85%, #8d8a72 100%);
  }
  .hero__brand-panel {
    position: absolute; left: 0; bottom: 0; width: 380px; height: 100px;
    background: linear-gradient(90deg, rgba(255,255,255,0.96) 0%, rgba(255,255,255,0.9) 55%, rgba(255,255,255,0) 100%);
    padding: 20px 0 0 24px;
  }
  .brand-name { font-family: 'Lato', sans-serif; font-weight: 700; font-size: 38px; color: var(--olive); line-height: 1; }
  .brand-tagline { margin-top: 8px; font-size: 14px; color: var(--ink); font-weight: 400; }

  .heading-factsheet {
    margin: 36px 0 0 19px;
    font-family: 'Oswald', sans-serif; font-weight: 700; font-size: 50px;
    color: var(--lime); line-height: 1;
  }

  .intro-band { margin-top: 22px; height: 68px; background: var(--blue); padding: 12px 26px 0 19px; }
  .intro-band p { color: var(--white); font-size: 16px; line-height: 1.3; text-align: justify; }

  .heading-section {
    margin: 26px 0 0 19px;
    font-family: 'Oswald', sans-serif; font-weight: 700; font-size: 34px;
    color: var(--blue); line-height: 1;
  }

  .nutrient-tables { display: flex; gap: 10px; margin: 14px 30px 0 19px; }
  .nutrient-table { flex: 1; border-collapse: separate; border-spacing: 0 4px; font-size: 14px; color: var(--ink); }
  .nutrient-table th { background: var(--lime); font-weight: 400; text-align: left; padding: 3px 8px; height: 24px; }
  .nutrient-table th.rate-value { text-align: center; }
  .nutrient-table td { background: var(--lime-light); padding: 3px 8px; line-height: 1.15; vertical-align: top; border-left: 4px solid var(--white); }
  .nutrient-table td:first-child { border-left: none; width: 42px; }
  .nutrient-table td.value { text-align: right; padding-right: 22px; }
  .nutrient-table td.value-alt { text-align: center; width: 88px; }

  .description { margin: 18px 30px 0 19px; font-size: 15.5px; line-height: 1.33; text-align: justify; color: var(--ink); }

  .benefits { position: absolute; left: 214px; right: 0; top: 814px; height: 298px; background: var(--blue); padding: 26px 0 0 40px; }
  .benefits ul { list-style: none; }
  .benefits li {
    position: relative; padding-left: 26px;
    font-family: 'Oswald', sans-serif; font-weight: 500; font-size: 25px;
    color: var(--white); line-height: 32px;
  }
  .benefits li::before { content: ""; position: absolute; left: 0; top: 13px; width: 8px; height: 8px; border-radius: 50%; background: var(--white); }

  .contact { position: absolute; left: 214px; right: 0; top: 1113px; height: 36px; display: flex; justify-content: space-between; padding: 2px 80px 0 50px; font-size: 13px; line-height: 1.3; color: var(--ink); }
  .contact__item { display: flex; gap: 8px; align-items: flex-start; }
  .contact__item svg { flex: none; margin-top: 2px; }

  .footer-band { position: absolute; left: 0; right: 0; top: 1150px; height: 50px; background: var(--lime); display: flex; align-items: center; justify-content: center; padding-left: 214px; }
  .footer-band span { font-weight: 700; font-size: 19px; letter-spacing: 9px; color: var(--olive); }
</style>
</head>
<body>
<main class="factsheet">
  <aside class="side-band"><div class="side-band__title">BIOSOLIDS+</div></aside>
  <div class="side-rule"></div>

  <section class="content">
    <header class="hero">
      <div class="hero__photo" role="img" aria-label="Photograph of young green crop rows in a field under a cloudy sky"></div>
      <div class="hero__brand-panel">
        <div class="brand-name">Greenward</div>
        <div class="brand-tagline">Feeding the soil, sparing the land...</div>
      </div>
    </header>

    <h1 class="heading-factsheet">FACTSHEET</h1>

    <div class="intro-band">
      <p>An environmentally friendly semi-dried fertiliser providing Nitrogen, Phosphate, Potash, Lime and organic matter to help improve your soils.</p>
    </div>

    <h2 class="heading-section">WHAT'S IN IT?</h2>

    <div class="nutrient-tables">
      <table class="nutrient-table">
        <tr><th>RATE</th><th class="rate-value" colspan="2">24T/HA</th></tr>
        <tr><td>N<br>P<br>K</td><td class="value">204<br>624<br>19</td><td class="value-alt">22<br>312<br>16</td></tr>
      </table>
      <table class="nutrient-table">
        <tr><th>RATE</th><th class="rate-value" colspan="2">24T/HA</th></tr>
        <tr><td>N<br>P<br>K</td><td class="value">204<br>624<br>19</td><td class="value-alt">22<br>312<br>16</td></tr>
      </table>
    </div>

    <p class="description">This is a by-product of wastewater treatment produced to a high standard in many plants across the UK. Following a full site assessment we deliver into temporary field stores (stockpiles) throughout the year ready for spreading at the optimum time. Nitrogen is of both readily available and slow releasing types enhancing plant growth and reducing the risk of nitrogen and phosphate leaching.</p>
  </section>

  <section class="benefits">
    <ul>
      <li>Recommended for Cereals, Maize and grazed grass</li>
      <li>Reduce the need for expensive artificial fertilisers</li>
      <li>Delivery and spreading included</li>
      <li>Improves soil structure</li>
      <li>Assists in maintaining pH</li>
      <li>All year round application (NVZ)</li>
      <li>Can be used with Norfibre</li>
    </ul>
  </section>

  <div class="contact">
    <div class="contact__item">
      <svg width="10" height="14" viewBox="0 0 10 14" aria-hidden="true"><path d="M5 0a5 5 0 0 0-5 5c0 3.8 5 9 5 9s5-5.2 5-9a5 5 0 0 0-5-5zm0 7a2 2 0 1 1 0-4 2 2 0 0 1 0 4z" fill="#1b63ad"/></svg>
      <span>Field Return Services Ltd Meadow House,<br>Meadow Lane, Brynteg, Northfield LL</span>
    </div>
    <div class="contact__item">
      <svg width="12" height="30" viewBox="0 0 12 30" aria-hidden="true">
        <path d="M2.5 0.5l2 0 1.2 3-1.4 1.2a7 7 0 0 0 3 3l1.2-1.4 3 1.2 0 2c0 .8-.7 1.5-1.5 1.5A10 10 0 0 1 1 2c0-.8.7-1.5 1.5-1.5z" fill="#1b63ad"/>
        <rect x="1" y="19" width="10" height="7" rx="1" fill="#1b63ad"/><rect x="3" y="16" width="6" height="3" fill="#1b63ad"/><rect x="3" y="24" width="6" height="4" fill="#ffffff" stroke="#1b63ad"/>
      </svg>
      <span>01632 960184<br>01632 960372</span>
    </div>
  </div>

  <footer class="footer-band"><span>www.fieldreturn.com</span></footer>
</main>
</body>
</html>
```